New Business Card Design Project

Make a kick ass business card for The Otter Tea Mug, using the designs. I also might like the 2nd place design logo on the back? Maybe all black with that? Not sure. Also, I'm cool with it being on metal, plastic, glass? or whatever for the business card. Maybe shaped like a shark? Let me know what else you need? Would like designs in the next day or so. Thank you.
Target Market(s)
Anyone that is cool
Contact Information for Business Card
Name: Dorian Fenwick
Phone: 317.594.8126
inventor/creator/entrepreneur/owner
www.theottertyeamug.example
social media links
https://www.facebook.com/theottertyeamug
https://twitter.com/otter_brew
https://www.instagram.com/theottertyeamug/
I'll get the Pinterest one soon
Colors
Designer to choose colors to be used in the design.
Requirements
Must have
- The Otter Tea Mug
- www.theottertyeamug.example
- social media tags?
- My logos and picture/photo of wine glass
Nice to have
- Maybe shaped like a wine glass or shark
- I'll let you decide but my same colors from my website would be nice

```html
<!DOCTYPE html>
<html lang="en">
<head>
<meta charset="utf-8">
<title>Otter Tea Mug – Business Card</title>
<link rel="stylesheet" href="https://fonts.googleapis.com/css2?family=PT+Sans:ital,wght@1,700&family=Raleway:wght@400&family=Yellowtail&display=block">
<style>
  :root {
    --silver-edge: #9aa1a8;
    --silver-mid: #cfd4d8;
    --silver-light: #f4f5f6;
    --name-red: #c0252f;
    --contact-plum: #8a3a5c;
    --icon-dark: #2b2b2b;
    --brand-grey: #707174;
    --bubble-tone: rgba(178,182,186,0.75);
  }
  html, body {
    margin: 0;
    padding: 0;
    width: 1200px;
    height: 777px;
    overflow: hidden;
    background: #ffffff;
  }
  .card {
    position: relative;
    width: 1200px;
    height: 777px;
    overflow: hidden;
    background: linear-gradient(90deg, var(--silver-edge) 0%, var(--silver-mid) 10%, var(--silver-light) 30%, var(--silver-mid) 62%, #e2e5e8 82%, var(--silver-edge) 100%);
  }
  .bubble-stream {
    position: absolute;
    left: 560px;
    top: 290px;
    width: 640px;
    height: 487px;
    background:
      radial-gradient(ellipse 70px 200px at 280px 130px, var(--bubble-tone) 0%, rgba(178,182,186,0) 100%),
      radial-gradient(ellipse 330px 200px at 300px 430px, var(--bubble-tone) 0%, rgba(178,182,186,0.35) 55%, rgba(178,182,186,0) 100%),
      radial-gradient(ellipse 200px 160px at 560px 420px, rgba(178,182,186,0.55) 0%, rgba(178,182,186,0) 100%);
  }
  .bubble-scatter {
    position: absolute;
    left: 0;
    top: 400px;
    width: 640px;
    height: 377px;
    background:
      radial-gradient(ellipse 60px 110px at 40px 80px, rgba(178,182,186,0.6) 0%, rgba(178,182,186,0) 100%),
      radial-gradient(ellipse 380px 90px at 360px 360px, rgba(178,182,186,0.6) 0%, rgba(178,182,186,0) 100%);
  }
  .owner-name {
    position: absolute;
    left: 114px;
    top: 122px;
    margin: 0;
    font-family: "Yellowtail", cursive;
    font-weight: 400;
    font-size: 80px;
    color: var(--name-red);
    line-height: 1;
  }
  .brand-mark {
    position: absolute;
    left: 852px;
    top: 112px;
    width: 70px;
    height: 70px;
    border-radius: 50%;
    background: var(--name-red);
  }
  .brand {
    position: absolute;
    left: 624px;
    width: 526px;
    top: 232px;
    margin: 0;
    font-family: "Raleway", sans-serif;
    font-weight: 400;
    font-size: 74px;
    color: var(--brand-grey);
    line-height: 1;
    text-align: center;
  }
  .contact-list {
    position: absolute;
    left: 113px;
    top: 0;
    margin: 0;
    padding: 0;
    list-style: none;
  }
  .contact-item {
    position: absolute;
    left: 0;
    display: flex;
    align-items: center;
    height: 80px;
    white-space: nowrap;
  }
  .contact-item:nth-child(1) { top: 250px; }
  .contact-item:nth-child(2) { top: 351px; }
  .contact-item:nth-child(3) { top: 450px; }
  .contact-item:nth-child(4) { top: 548px; }
  .contact-item:nth-child(5) { top: 646px; }
  .contact-icon {
    width: 76px;
    height: 76px;
    flex: none;
  }
  .contact-text {
    margin-left: 28px;
    font-family: "PT Sans", sans-serif;
    font-style: italic;
    font-weight: 700;
    font-size: 37px;
    color: var(--contact-plum);
  }
</style>
</head>
<body>
<main class="card">
  <div class="bubble-scatter" role="img" aria-label="Faint scattered bubble pattern"></div>
  <div class="bubble-stream" role="img" aria-label="Grey bubble pattern rising like poured wine"></div>

  <h1 class="owner-name">Dorian Fenwick</h1>
  <div class="brand-mark" aria-hidden="true"></div>
  <p class="brand">Otter Tea Mug</p>

  <ul class="contact-list">
    <li class="contact-item">
      <svg class="contact-icon" viewBox="0 0 76 76" aria-hidden="true">
        <circle cx="38" cy="38" r="34" fill="var(--icon-dark)"/>
        <path d="M28 20c3 0 5 6 6 9s-3 5-3 7c2 5 6 9 11 11 2 0 4-4 7-3s8 3 8 6-4 8-8 8C35 58 20 43 20 28c0-4 5-8 8-8z" fill="#eef0f2"/>
      </svg>
      <span class="contact-text">317.594.8126</span>
    </li>
    <li class="contact-item">
      <svg class="contact-icon" viewBox="0 0 76 76" aria-hidden="true" fill="none" stroke="var(--icon-dark)" stroke-width="6">
        <circle cx="38" cy="38" r="32"/>
        <ellipse cx="38" cy="38" rx="14" ry="32"/>
        <line x1="6" y1="38" x2="70" y2="38"/>
      </svg>
      <span class="contact-text">www.theottertyeamug.example</span>
    </li>
    <li class="contact-item">
      <svg class="contact-icon" viewBox="0 0 76 76" aria-hidden="true">
        <rect x="6" y="6" width="64" height="64" rx="14" fill="var(--icon-dark)"/>
      </svg>
      <span class="contact-text">theottertyeamug</span>
    </li>
    <li class="contact-item">
      <svg class="contact-icon" viewBox="0 0 76 76" aria-hidden="true">
        <rect x="6" y="6" width="64" height="64" rx="14" fill="var(--icon-dark)"/>
      </svg>
      <span class="contact-text">The Otter Tea Mug</span>
    </li>
    <li class="contact-item">
      <svg class="contact-icon" viewBox="0 0 76 76" aria-hidden="true">
        <rect x="6" y="6" width="64" height="64" rx="14" fill="var(--icon-dark)"/>
      </svg>
      <span class="contact-text">The Otter Tea Mug</span>
    </li>
  </ul>
</main>
</body>
</html>
```